A3 Internet Cafe advertising posters required - Targetting South Asian & Filipino customers

An internet cafe based within a male-only labour accomodation facility in the United Arab Emirates needs to advertise its presence and services to the employees who live at the facility.

The cafe is called "The Net Nook" and it offers customers the opportunity to use high-speed broadband internet to engage in activities such as Vocalo Web Cam chat with family back home, email, mingleweb, etc, as well as movies and other entertainment from a variety of countries including India. Customers can also purchase refreshments such as biscuits, cakes, tea, 'chai karak' (a local kind of tea), cold soft drinks.

The cost of the internet at the cafe is 5 AED per hour, however users can purchase 10 hours for 40 AED - which should be promoted as a special offer, and these 10 hours can be used whenever the user wishes with no validity limits.

The poster should seek to inform and promote the cafe, the opening hours of the cafe are 11AM - 12AM (MIDNIGHT) every day.

Target Market(s)

male, semi skilled labourers, mostly indian, pakistani with significant filipino proportion

Industry/Entity Type

Entertainment

Requirements
Must have
• photo - centric, the customers are mostly semi-skilled labourers with limited grasp of english, photos that communicate the concepts of watching movies, having tea, speaking to family back home via a computer would work best.
Should not have
• anything sexually suggestive

```html
<!DOCTYPE html>
<html lang="en">
<head>
<meta charset="utf-8">
<title>The Net Nook – Internet Cafe</title>
<link rel="stylesheet" href="https://fonts.googleapis.com/css2?family=Montserrat:wght@300;400;700&family=Crimson+Pro:wght@600;700&display=swap">
<style>
  :root {
    --navy-deep: #0b0c2c;
    --navy: #1a1f4e;
    --brand-blue: #1b6fe0;
    --white: #ffffff;
    --rule: #c9cbe0;
    --teal-light: #a9dedd;
    --teal: #7ec6c7;
    --teal-dark: #5fb0b3;
    --panel: rgba(236, 246, 246, 0.93);
    --ink: #111318;
    --strip: #f6f2f2;
  }
  * { margin: 0; padding: 0; box-sizing: border-box; }
  html, body { width: 848px; height: 1200px; overflow: hidden; }
  body { font-family: "Crimson Pro", Georgia, serif; color: var(--ink); }

  .poster { position: relative; width: 848px; height: 1200px; overflow: hidden;
    background: linear-gradient(160deg, var(--teal-light) 0%, var(--teal) 45%, var(--teal-dark) 100%); }

  .masthead { position: absolute; left: 0; top: 0; width: 848px; height: 374px;
    background: radial-gradient(ellipse at 50% 0%, var(--navy) 0%, var(--navy-deep) 75%);
    color: var(--white); text-align: center; font-family: "Montserrat", Arial, sans-serif; }
  .masthead .brand-dot { position: absolute; left: 370px; top: 40px; }
  .masthead .brand-name { position: absolute; top: 160px; width: 100%; font-size: 49px; font-weight: 700; letter-spacing: 0.5px; }
  .masthead .brand-type { position: absolute; top: 212px; width: 100%; font-size: 33px; font-weight: 400; }
  .masthead .divider { position: absolute; left: 174px; top: 262px; width: 540px; height: 2px;
    background: linear-gradient(90deg, transparent, var(--rule), transparent); }
  .masthead .hours-label { position: absolute; top: 282px; width: 100%; font-size: 29px; font-weight: 700; color: var(--brand-blue); }
  .masthead .hours { position: absolute; top: 318px; width: 100%; font-size: 31px; font-weight: 300; letter-spacing: 0.5px; }

  .panel { position: absolute; background: var(--panel); }
  .panel-rate { left: 0; top: 432px; width: 428px; height: 86px; display: flex; align-items: center; justify-content: center;
    font-size: 28px; font-weight: 700; }
  .panel-offer { left: 454px; top: 400px; width: 394px; height: 171px; text-align: center; }
  .panel-offer .title { margin-top: 18px; font-size: 28px; font-weight: 700; color: var(--brand-blue); }
  .panel-offer .deal { margin-top: 12px; font-size: 29px; font-weight: 700; }
  .panel-offer .note { font-size: 16px; font-weight: 700; line-height: 1.2; }

  .panel-services { left: 0; top: 554px; width: 428px; height: 336px; }
  .panel-services .lead { margin: 62px 0 0 34px; font-size: 17px; font-weight: 700; color: var(--brand-blue); }
  .panel-services ul { list-style: none; margin: 24px 0 0 76px; font-size: 25px; font-weight: 700; line-height: 34px; }

  .panel-shop { left: 454px; top: 620px; width: 394px; height: 336px; }
  .panel-shop .title { margin: 52px 0 0 100px; font-size: 29px; font-weight: 700; color: var(--brand-blue); }
  .panel-shop ul { list-style: none; margin: 20px 0 0 100px; font-size: 25px; font-weight: 700; line-height: 36px; }

  .photo-strip { position: absolute; left: 0; top: 978px; width: 848px; height: 222px; background: var(--strip); }
  .photo { position: absolute; top: 1000px; height: 170px; }
  .photo-entrance { left: 17px; width: 231px; background: linear-gradient(180deg, #d9dcd8, #b9bfb9); }
  .photo-hall-a { left: 266px; width: 130px; background: linear-gradient(180deg, #8a8a86, #cfc4b4); }
  .photo-hall-b { left: 412px; width: 128px; background: linear-gradient(180deg, #7f807c, #d6c8b5); }
  .photo-night { left: 556px; width: 130px; background: linear-gradient(180deg, #29302a, #4a5348 60%, #b8b6ad); }
  .photo-counter { left: 702px; width: 130px; background: linear-gradient(180deg, #7a837e, #b9b6a8); }
</style>
</head>
<body>
<main class="poster">
  <header class="masthead">
    <svg class="brand-dot" width="108" height="108" viewBox="0 0 108 108" aria-hidden="true">
      <circle cx="54" cy="54" r="54" fill="#1b6fe0"/>
    </svg>
    <h1 class="brand-name">The Net Nook</h1>
    <p class="brand-type">Internet Cafe</p>
    <div class="divider"></div>
    <p class="hours-label">OPENS</p>
    <p class="hours">11AM - 12AM (MIDNIGHT) daily</p>
  </header>

  <section class="panel panel-rate">5 AED per hour</section>

  <section class="panel panel-offer">
    <h2 class="title">Special offer!</h2>
    <p class="deal">10 hours for 40 AED</p>
    <p class="note">-can be used whenever the user<br>wishes with no validity limits.</p>
  </section>

  <section class="panel panel-services">
    <p class="lead">high-speed broadband internet for</p>
    <ul>
      <li>Vocalo Web Cam chat</li>
      <li>email</li>
      <li>mingleweb, etc</li>
      <li>as well as movies and</li>
      <li>other entertainment</li>
    </ul>
  </section>

  <section class="panel panel-shop">
    <h2 class="title">We also Sell</h2>
    <ul>
      <li>biscuits</li>
      <li>cakes</li>
      <li>tea</li>
      <li>'chai karak'</li>
      <li>cold soft drinks.</li>
    </ul>
  </section>

  <footer class="photo-strip"></footer>
  <div class="photo photo-entrance" role="img" aria-label="Photo of the cafe's glass entrance doors"></div>
  <div class="photo photo-hall-a" role="img" aria-label="Photo of rows of computer desks inside the cafe"></div>
  <div class="photo photo-hall-b" role="img" aria-label="Photo of the long computer hall with tiled floor"></div>
  <div class="photo photo-night" role="img" aria-label="Photo of the cafe front lit up at night"></div>
  <div class="photo photo-counter" role="img" aria-label="Photo of the refreshment counter with a drinks fridge"></div>
</main>
</body>
</html>
```